christmas poster

Gift Vouchers Promotion

Buy 3 of Any Value
Get 1 More Free

The Poster Should be very modern but with a relevance to Christmas

Target Market(s)

Affluent Clients

Font styles to use
Decorative

Colors
ec1f27

Requirements
Must have
• Modern Clean Feel but Relevant to Christmas
Nice to have
• The Offer:
• Buy 3 Gift Vouchers and Receive 1 More Fee
• MUST be Big and Bold
• Include Logo

```html
<!DOCTYPE html>
<html lang="en">
<head>
<meta charset="utf-8">
<title>Gift Vouchers – Buy 3 &amp; Receive 1 More Free</title>
<link rel="stylesheet" href="https://fonts.googleapis.com/css2?family=Bebas+Neue&family=Pinyon+Script&display=swap">
<style>
  :root {
    --festive-red: #ec1f27;
    --filigree-tone: #5a0b0f;
    --brand-red: #d71f2b;
    --ink: #111111;
    --gold: #a98838;
    --gold-shadow: #c9a54e;
    --paper: #ffffff;
  }
  html, body {
    margin: 0;
    padding: 0;
    overflow: hidden;
    background: var(--paper);
  }
  .poster {
    position: relative;
    width: 849px;
    height: 1200px;
    overflow: hidden;
    background: linear-gradient(to bottom,
      var(--festive-red) 0%,
      var(--festive-red) 53%,
      var(--paper) 67%,
      var(--paper) 100%);
  }
  .ornament {
    position: absolute;
    left: 0;
    top: 0;
    width: 849px;
    height: 800px;
  }
  .voucher-title {
    position: absolute;
    left: 170px;
    top: 331px;
    width: 506px;
    height: 148px;
    display: flex;
    align-items: center;
    justify-content: center;
    margin: 0;
    font-family: "Pinyon Script", cursive;
    font-weight: 400;
    font-size: 68px;
    color: var(--ink);
    letter-spacing: 1px;
  }
  .offer {
    position: absolute;
    left: 0;
    top: 800px;
    width: 849px;
    margin: 0;
    text-align: center;
    font-family: "Bebas Neue", sans-serif;
    font-weight: 400;
    font-size: 98px;
    line-height: 86px;
    letter-spacing: 2px;
    color: var(--ink);
    text-shadow: 4px 4px 0 var(--gold-shadow);
  }
  .brand {
    position: absolute;
    left: 0;
    top: 1022px;
    width: 849px;
    text-align: center;
    font-family: "Bebas Neue", sans-serif;
    font-weight: 400;
    color: var(--brand-red);
  }
  .brand-name {
    display: block;
    font-size: 100px;
    line-height: 96px;
    letter-spacing: 3px;
  }
  .brand-line {
    display: block;
    font-size: 36px;
    line-height: 42px;
    letter-spacing: 14px;
    margin-top: 2px;
  }
</style>
</head>
<body>
  <main class="poster">
    <svg class="ornament" viewBox="0 0 849 800" role="img" aria-label="Black Christmas baroque filigree flourish framing the gift voucher label">
      <defs>
        <radialGradient id="filigreeGlow" cx="50%" cy="50%" r="50%">
          <stop offset="0%" stop-color="var(--filigree-tone)" stop-opacity="0.55"/>
          <stop offset="75%" stop-color="var(--filigree-tone)" stop-opacity="0.4"/>
          <stop offset="100%" stop-color="var(--filigree-tone)" stop-opacity="0"/>
        </radialGradient>
      </defs>
      <ellipse cx="424.5" cy="405" rx="330" ry="345" fill="url(#filigreeGlow)"/>
      <rect class="dotted-frame" x="311" y="275" width="272" height="260"
            fill="none" stroke="var(--ink)" stroke-width="3" stroke-dasharray="2 6"/>
      <g class="voucher-label">
        <path d="M144 340 Q164 340 166 306 L683 306 Q685 340 705 340 L705 475 Q685 475 683 509 L166 509 Q164 475 144 475 Z"
              fill="var(--festive-red)" stroke="var(--ink)" stroke-width="3"/>
        <path d="M170 331 L676 331 L676 479 L170 479 Z" fill="var(--gold)" stroke="var(--ink)" stroke-width="2"/>
      </g>
    </svg>

    <h2 class="voucher-title">Gift Vouchers</h2>

    <h1 class="offer">Buy 3 &amp; Receive<br>1 More Free</h1>

    <div class="brand">
      <span class="brand-name">velora</span>
      <span class="brand-line">salon &amp; spa</span>
    </div>
  </main>
</body>
</html>
```